improvement on my landing page

We are a fansite platform similar to velbrook.com, quindleo.com , tarvimu.com and gorbelix.com. We are aiming to disrupt this space by a much cheaper and advanced platform to help influencers monetise across different tools.

current lander is https://plumvarra.com/

Looking for a modern, clean, feminine , pink. Current style and other competitors list given feel old and this needs to highlight its a cutting edge product replacing them. Designs I like are www.brisko.app for example.

I need a few elaborations from current site on price differences of competitors, icons and more details on features and several other new sections added. Need a form to capture email , name and phone as this is a coming soon page. Can change later as a signup

attached document is how thee site looks, so need to keep the identity

Target Market(s)

influence's, adult

Font styles to use
Sans Serif

Colors
eea4c8
fefafc
ecdaeb

Requirements
Nice to have
• infographics

```html
<!DOCTYPE html>
<html lang="en">
<head>
<meta charset="utf-8">
<title>Plumvarra – Keep 90% of your earnings</title>
<link href="https://fonts.googleapis.com/css2?family=Lato:wght@400;700;900&display=swap" rel="stylesheet">
<style>
:root{
  --pink:#ec1d67;
  --pink-soft:#eea4c8;
  --blush:#fefafc;
  --lilac:#ecdaeb;
  --icon-bg:#ecd6e6;
  --ink:#1d1d22;
  --grey:#6d6d74;
  --line:#c9c9cf;
  --panel:#f3f3f4;
}
*{box-sizing:border-box;margin:0;padding:0}
html,body{width:1200px;height:3834px;overflow:hidden}
body{font-family:'Lato',sans-serif;color:var(--ink);background:var(--blush)}
.page{position:relative;width:1200px;height:3834px;overflow:hidden;background:#fff}
.abs{position:absolute}

/* header */
.brand{left:127px;top:30px;display:flex;align-items:center;gap:10px;font-weight:700;font-size:21px;letter-spacing:.5px;z-index:2}
.brand-dot{width:26px;height:26px;background:var(--ink);border-radius:50%;flex:none}
.btn{display:flex;align-items:center;justify-content:center;background:var(--pink);color:#fff;font-weight:700;border-radius:8px;box-shadow:0 4px 10px rgba(236,29,103,.3);text-transform:uppercase}
.join{left:907px;top:29px;width:119px;height:31px;font-size:12px}
.login{left:1050px;top:36px;font-size:12px;font-weight:700;display:flex;gap:8px;align-items:center}

/* hero */
.hero-bg{left:0;top:0}
.hero-title{left:127px;top:220px;font-size:28px;font-weight:700;line-height:37px;z-index:2;white-space:nowrap}
.hero-text{left:127px;top:309px;font-size:11.5px;line-height:19px;color:#3b3b40;z-index:2;white-space:nowrap}
.started{left:127px;top:362px;width:122px;height:33px;font-size:12px;z-index:2}
.learn{left:293px;top:368px;font-size:12px;font-weight:700;color:var(--pink);border-bottom:1px solid var(--pink);padding-bottom:2px;z-index:2}
.mock{left:0;top:0}

/* section headings */
.sec-title{left:0;width:1200px;text-align:center;font-size:21px;font-weight:700}
.sec-sub{left:0;width:1200px;text-align:center;font-size:10px;color:#555}
.bar{width:68px;height:3px;background:var(--pink);left:566px}

/* why */
.why-name{left:179px;top:803px;font-size:34px;font-weight:400;letter-spacing:1px}
.why-text{left:113px;top:910px;width:460px;font-size:12.5px;line-height:25px;color:#55555b;white-space:nowrap}
.dots{display:grid;gap:0}
.dots span{width:3px;height:3px;border-radius:50%;background:#c7c7cc;display:block}
.mark{left:790px;top:830px;width:200px;height:200px;border-radius:50%;background:linear-gradient(140deg,#e8a9c5,#cd7ea3)}

/* features */
.features-bg{left:0;top:1310px;width:1200px;height:1100px;background:var(--blush)}
.card{width:245px;height:261px;background:#fff;border-radius:24px;box-shadow:0 6px 16px rgba(0,0,0,.12);text-align:center}
.card .ico{width:113px;height:113px;border-radius:50%;background:var(--icon-bg);margin:30px auto 0;display:flex;align-items:center;justify-content:center}
.card h3{font-size:17px;font-weight:700;margin-top:24px;line-height:21px;padding:0 20px}
.card p{font-size:11px;color:var(--grey);line-height:18px;margin-top:8px;padding:0 30px}
.link{height:0;border-top:4px dotted #7b7b80}

/* fees */
.rule{height:1px;background:var(--pink-soft)}
.col-head{top:2610px;width:150px;text-align:center;font-size:11px;letter-spacing:.5px;color:#333}
.logo-row{left:225px;top:2638px;width:624px;height:57px;background:#f1f1f2}
.logo-name{top:2655px;width:150px;text-align:center;font-size:14px;font-weight:700;color:#e7a8c4}
.fee-row{left:112px;top:2695px;width:737px;height:98px;background:#f3f3f4;border-top:2px solid #bbb}
.fee-label{left:133px;top:2732px;font-size:18px;font-weight:700}
.fee{top:2733px;width:155px;text-align:center;font-size:18px;font-weight:700}
.vsep{top:2710px;width:1px;height:68px;background:#bbb}
.ours{left:849px;top:2637px;width:207px;height:156px;background:#fff;box-shadow:0 4px 14px rgba(0,0,0,.15)}
.ours-name{left:890px;top:2662px;display:flex;gap:8px;align-items:center;font-size:16px;font-weight:700}
.ours-fee{left:919px;top:2700px;width:68px;height:68px;border-radius:50%;background:var(--pink);color:#fff;font-size:24px;font-weight:700;display:flex;align-items:center;justify-content:center}
.saving{left:521px;top:2840px;width:157px;height:44px;font-size:14px}

/* signup */
.field{left:454px;width:291px;height:45px;border-radius:12px;background:#fff;display:flex;align-items:center;gap:12px;padding-left:26px;font-size:12px;color:#a9a9af}
.register{left:454px;top:3505px;width:291px;height:45px;border-radius:12px;font-size:14px;font-weight:400}

/* footer */
.play{left:0;width:1200px;top:3700px;text-align:center;font-size:21px;font-weight:700;color:#f6dce9}
.nav a{position:absolute;top:3745px;font-size:12px;color:#222;text-decoration:none;transform:translateX(-50%)}
.foot-brand{left:74px;top:3776px;display:flex;gap:14px;align-items:center;font-size:10px}
.legal{top:3782px;font-size:12px;color:#222;transform:translateX(-50%)}
</style>
</head>
<body>
<div class="page">

  <!-- hero background -->
  <svg class="abs hero-bg" width="1200" height="700" viewBox="0 0 1200 700">
    <path d="M0 0 H560 Q660 60 640 200 Q635 280 560 320 L80 640 Q30 665 0 650 Z" fill="#f5f5f6"/>
    <path d="M0 640 Q30 665 80 640 L90 636 Q40 660 0 655 Z" fill="#e9e9eb"/>
  </svg>

  <section class="hero">
    <svg class="abs mock" width="1200" height="700" viewBox="0 0 1200 700" role="img" aria-label="Creator profile app screen tilted in perspective, with a portrait photo, subscribe, private chat, Snaplume, tip and custom request options">
      <defs>
        <linearGradient id="mockFill" x1="0" y1="0" x2="1" y2="1">
          <stop offset="0" stop-color="#ffffff"/>
          <stop offset=".6" stop-color="#f7eef3"/>
          <stop offset="1" stop-color="#eea4c8"/>
        </linearGradient>
      </defs>
      <path d="M700 205 L905 135 L1100 380 L660 650 L445 515 Z" fill="url(#mockFill)" stroke="#ececef" stroke-width="6" stroke-linejoin="round"/>
    </svg>
    <h1 class="abs hero-title">KEEP 90% OF YOUR EARNINGS<br>NO HIDDEN FEES.</h1>
    <p class="abs hero-text">Make more with added revenue streams and features for <b>FREE.</b><br>Maximise you're your fanbase profits with Plumvarra.</p>
    <a class="abs btn started">Get started</a>
    <a class="abs learn">Learn More ▸</a>
  </section>

  <header>
    <div class="abs brand"><span class="brand-dot"></span>PLUMVARRA</div>
    <a class="abs btn join">Join free</a>
    <div class="abs login">
      <svg width="14" height="14" viewBox="0 0 14 14"><rect x="2" y="6" width="10" height="7" rx="1.5" fill="none" stroke="#ec1d67" stroke-width="1.6"/><path d="M4.5 6V4a2.5 2.5 0 0 1 5 0v2" fill="none" stroke="#ec1d67" stroke-width="1.6"/></svg>
      LOGIN
    </div>
  </header>

  <section class="why">
    <svg class="abs" style="left:190px;top:680px" width="1000" height="600" viewBox="0 0 1000 600">
      <path d="M20 60 Q20 -10 90 30 L185 90 Q220 115 190 140 L80 210 Q20 245 20 170 Z" fill="#f6f6f7"/>
      <path d="M460 340 Q440 320 470 300 L850 60 Q930 10 935 100 L935 520 Q935 600 860 560 Z" fill="#f4f4f5" stroke="#e6e6e8" stroke-width="4"/>
    </svg>
    <h2 class="abs sec-title" style="top:718px">WHY CHOOSE US?</h2>
    <div class="abs bar" style="top:756px"></div>
    <div class="abs dots" style="left:15px;top:808px;grid-template-columns:repeat(5,3px);column-gap:23px;row-gap:20px">
      <span></span><span></span><span></span><span></span><span></span>
      <span></span><span></span><span></span><span></span><span></span>
      <span></span><span></span><span></span><span></span><span></span>
    </div>
    <h2 class="abs why-name">PLUMVARRA</h2>
    <p class="abs why-text">Plumvarra was developed to democratise the fan platform space.<br>As entrepreurs ourselves we don't see why you should you be handing<br>over a high percentage of your hard earned profits to platforms with<br>mediocre features and services. Receive 90% of your earnings,<br>with no hidden fees or extras AND with fastest payouts.<br>Monetize with monthly subscriptions through private profile feeds and<br>premium social media accounts. Private messaging and tipping,<br>premium videos and much more.<br>Start earning more and keeping your profits.</p>
    <div class="abs dots" style="left:546px;top:1127px;grid-template-columns:repeat(5,3px);column-gap:23px;row-gap:18px">
      <span></span><span></span><span></span><span></span><span></span>
      <span></span><span></span><span></span><span></span><span></span>
      <span></span><span></span><span></span><span></span><span></span>
    </div>
    <div class="abs mark" role="img" aria-label="Plumvarra brand emblem"></div>
  </section>

  <section class="features">
    <div class="abs features-bg"></div>
    <svg class="abs" style="left:0;top:2190px" width="1200" height="450" viewBox="0 0 1200 450">
      <path d="M0 0 Q250 100 270 220 Q280 330 0 420 Z" fill="#f3f3f4"/>
      <path d="M1200 0 Q950 100 925 220 Q915 330 1200 420 Z" fill="#f3f3f4"/>
    </svg>
    <h2 class="abs sec-title" style="top:1253px">HOW IT WORKS</h2>
    <div class="abs bar" style="top:1287px"></div>

    <div class="abs link" style="left:380px;top:1480px;width:95px;transform:rotate(-7deg)"></div>
    <div class="abs link" style="left:722px;top:1482px;width:106px;transform:rotate(6deg)"></div>
    <div class="abs link" style="left:372px;top:1812px;width:100px;transform:rotate(7deg)"></div>
    <div class="abs link" style="left:722px;top:1808px;width:106px;transform:rotate(-7deg)"></div>
    <div class="abs link" style="left:372px;top:2110px;width:100px;transform:rotate(5deg)"></div>
    <div class="abs link" style="left:722px;top:2108px;width:106px;transform:rotate(-5deg)"></div>

    <div class="abs card" style="left:127px;top:1400px">
      <div class="ico"><svg width="60" height="40" viewBox="0 0 60 40"><rect x="2" y="6" width="56" height="28" rx="3" fill="#fff"/><circle cx="30" cy="20" r="8" fill="#ecd6e6"/><rect x="8" y="16" width="6" height="8" fill="#ecd6e6"/><rect x="46" y="16" width="6" height="8" fill="#ecd6e6"/></svg></div>
      <h3>FASTEST PAYOUT</h3><p>Get your money in less than 7 days</p>
    </div>
    <div class="abs card" style="left:475px;top:1379px">
      <div class="ico"><svg width="60" height="50" viewBox="0 0 60 50"><circle cx="22" cy="14" r="10" fill="#fff"/><path d="M2 46 Q4 28 22 28 Q34 28 38 36 L38 46 Z" fill="#fff"/><circle cx="46" cy="38" r="9" fill="none" stroke="#fff" stroke-width="4" stroke-dasharray="4 3"/><circle cx="46" cy="38" r="3" fill="#fff"/></svg></div>
      <h3>CUSTOMIZABLE SUBSCRIPTION</h3><p>Build your own subscription plan to fit your business.</p>
    </div>
    <div class="abs card" style="left:828px;top:1400px">
      <div class="ico"><svg width="64" height="64" viewBox="0 0 64 64"><circle cx="32" cy="32" r="27" fill="none" stroke="#fff" stroke-width="5"/><path d="M42 23 A13 13 0 1 0 42 41" fill="none" stroke="#fff" stroke-width="7"/></svg></div>
      <h3>COPYRIGHT PROTECTION</h3><p>You own content, take it down whenever you want</p>
    </div>

    <div class="abs card" style="left:127px;top:1697px">
      <div class="ico"><svg width="60" height="64" viewBox="0 0 60 64"><circle cx="30" cy="12" r="9" fill="#fff"/><path d="M22 24 H38 V40 H34 V52 H26 V40 H22 Z" fill="#fff"/><ellipse cx="30" cy="56" rx="26" ry="6" fill="none" stroke="#fff" stroke-width="3"/></svg></div>
      <h3>GEO BLOCKING</h3><p>Hide your content from specific contries</p>
    </div>
    <div class="abs card" style="left:475px;top:1697px">
      <div class="ico"><svg width="64" height="54" viewBox="0 0 64 54"><circle cx="22" cy="27" r="19" fill="#fff"/><text x="22" y="34" text-anchor="middle" font-size="20" font-weight="700" fill="#ecd6e6" font-family="Lato,sans-serif">$</text><path d="M36 20 H60 V38 H40 Z" fill="#fff"/></svg></div>
      <h3>TIPS</h3><p>Increase your revenue stream without lifting a finger</p>
    </div>
    <div class="abs card" style="left:828px;top:1697px">
      <div class="ico"><svg width="54" height="54" viewBox="0 0 54 54"><rect x="4" y="14" width="46" height="32" rx="6" fill="#fff"/><rect x="18" y="8" width="18" height="10" rx="3" fill="#fff"/><circle cx="27" cy="30" r="9" fill="#ecd6e6"/></svg></div>
      <h3>PRIVATE<br>SNAPLUME</h3><p>Easily sell private Snaplume access &amp; monitor subscriptions</p>
    </div>

    <div class="abs card" style="left:127px;top:1995px">
      <div class="ico"><svg width="64" height="56" viewBox="0 0 64 56"><path d="M32 4 C50 4 60 14 60 25 C60 37 48 46 32 46 C28 46 24 45 21 44 L8 52 L12 40 C6 36 4 31 4 25 C4 14 14 4 32 4 Z" fill="#fff"/><circle cx="20" cy="25" r="3.5" fill="#ecd6e6"/><circle cx="32" cy="25" r="3.5" fill="#ecd6e6"/><circle cx="44" cy="25" r="3.5" fill="#ecd6e6"/></svg></div>
      <h3>PRIVATE MESSAGING</h3><p>Engage with your fans on a personal level. Your choice</p>
    </div>
    <div class="abs card" style="left:475px;top:2015px">
      <div class="ico"><svg width="50" height="60" viewBox="0 0 50 60"><ellipse cx="25" cy="10" rx="22" ry="8" fill="#fff"/><path d="M3 16 Q25 28 47 16 V28 Q25 40 3 28 Z" fill="#fff"/><path d="M3 34 Q25 46 47 34 V48 Q25 60 3 48 Z" fill="#fff"/></svg></div>
      <h3>INTELLEGENT<br>BUSINESS DATA</h3><p>Easily monitor your business &amp; learn from your intuitive data</p>
    </div>
    <div class="abs card" style="left:828px;top:1995px">
      <div class="ico"><svg width="54" height="62" viewBox="0 0 54 62"><path d="M27 4 C40 4 44 16 44 28 V40 L50 48 H4 L10 40 V28 C10 16 14 4 27 4 Z" fill="#fff"/><circle cx="27" cy="54" r="6" fill="#fff"/></svg></div>
      <h3>INSTANT<br>NOTIFICATIONS</h3><p>Never miss a beat. Get custom &amp; instant email updates.</p>
    </div>
  </section>

  <section class="fees">
    <div class="abs rule" style="left:365px;top:2412px;width:470px"></div>
    <h2 class="abs sec-title" style="top:2495px">FEE COMPARISON</h2>
    <div class="abs bar" style="top:2538px"></div>

    <div class="abs col-head" style="left:226px">VELBROOK</div>
    <div class="abs col-head" style="left:381px">QUINDLEO</div>
    <div class="abs col-head" style="left:531px">MODRELLA</div>
    <div class="abs col-head" style="left:690px">TARVIMU</div>
    <div class="abs col-head" style="left:873px">PLUMVARRA</div>

    <div class="abs logo-row"></div>
    <div class="abs logo-name" style="left:226px">Velbrook</div>
    <div class="abs logo-name" style="left:381px">Quindleo</div>
    <div class="abs logo-name" style="left:531px">Modrella</div>
    <div class="abs logo-name" style="left:690px">Tarvimu</div>

    <div class="abs fee-row"></div>
    <div class="abs fee-label">FEES <span style="color:#e7a8c4;font-size:11px;font-weight:400;margin-left:14px">ⓘ</span></div>
    <div class="abs vsep" style="left:225px"></div>
    <div class="abs vsep" style="left:378px"></div>
    <div class="abs vsep" style="left:533px"></div>
    <div class="abs vsep" style="left:688px"></div>
    <div class="abs fee" style="left:219px">8% - 15%</div>
    <div class="abs fee" style="left:378px">20%</div>
    <div class="abs fee" style="left:530px">25% - 35%</div>
    <div class="abs fee" style="left:688px">42.5%</div>

    <div class="abs ours"></div>
    <div class="abs ours-name"><span class="brand-dot" style="width:18px;height:18px"></span>PLUMVARRA</div>
    <div class="abs ours-fee">10%</div>

    <a class="abs btn saving">START SAVING!</a>
    <div class="abs rule" style="left:225px;top:2942px;width:750px"></div>
  </section>

  <section class="signup">
    <svg class="abs" style="left:0;top:2880px" width="1200" height="840" viewBox="0 0 1200 840">
      <path d="M0 30 Q120 220 360 240 Q560 255 760 190 Q980 120 1200 20 V840 H0 Z" fill="#eea4c8"/>
      <path d="M0 260 Q200 160 450 200 Q700 240 900 200 Q1080 170 1200 200 V700 Q900 620 600 660 Q300 700 0 720 Z" fill="#ecdaeb"/>
      <path d="M0 720 Q300 700 600 660 Q900 620 1200 700 V840 H0 Z" fill="#fefafc"/>
      <path d="M0 600 Q120 700 340 690 Q600 680 820 640 Q1000 610 1200 650 V840 H0 Z" fill="#eea4c8" opacity=".55"/>
      <path d="M0 760 Q300 735 620 700 Q920 670 1200 730 V840 H0 Z" fill="#fefafc"/>
    </svg>
    <h2 class="abs sec-title" style="top:2996px">CREATE YOUR FREE ACCOUNT</h2>
    <p class="abs sec-sub" style="top:3027px">IT ONLY TAKES A FEW SECONDS. NO CREDIT CARD REQUIRED.</p>
    <div class="abs bar" style="top:3051px"></div>

    <div class="abs field" style="top:3215px"><svg width="14" height="14" viewBox="0 0 14 14"><circle cx="7" cy="4" r="3.5" fill="#b5b5ba"/><path d="M0 14 Q1 8 7 8 Q13 8 14 14 Z" fill="#b5b5ba"/></svg>Your Name</div>
    <div class="abs field" style="top:3290px"><span style="font-size:14px">@</span>Your Email</div>
    <div class="abs field" style="top:3363px"><svg width="14" height="14" viewBox="0 0 14 14"><path d="M3 1 L5 4 L4 6 Q5 9 8 10 L10 9 L13 11 L11 13 Q4 13 1 3 Z" fill="#b5b5ba"/></svg>Your Phone</div>
    <div class="abs field" style="top:3434px"><svg width="14" height="14" viewBox="0 0 14 14"><circle cx="10" cy="4" r="3.5" fill="#b5b5ba"/><path d="M8 6 L1 13 L3 13 L4 12 L5 13 L6 11 L9 7 Z" fill="#b5b5ba"/></svg>Your Password</div>
    <a class="abs btn register">REGISTER</a>
  </section>

  <footer>
    <div class="abs play">PLAY WITH ME</div>
    <nav class="nav">
      <a style="left:453px">VIDEOS</a>
      <a style="left:539px">STARS</a>
      <a style="left:639px">CONTACT US</a>
      <a style="left:737px">F.A.Q.</a>
    </nav>
    <div class="abs foot-brand"><span class="brand-dot" style="width:30px;height:30px"></span>Thousands of content creators %100 verified</div>
    <div class="abs legal" style="left:935px">TERMS &amp; CONDITIONS</div>
    <div class="abs legal" style="left:1083px">PRIVACY POLICY</div>
  </footer>

</div>
</body>
</html>
```